iOS App Design Project for Pebble Notes

We are looking for a redesign of the UI for our app, Pebble Notes. The app is a to-do list type app with 4 screens, and we already have a UI for it but we would like a nicer looking one that has a better colour scheme and is more intuitive.

We would like something that is a real treat to look at, and that users really want to use. Essentially what we want is the nicest and most simple design possible, as the current UI we have is not very user friendly.

The app is already on the market and is free so if you have an iOS device you can download it and take a look at it, and we have also included screenshots of the app.
Updates

Project Deadline Extended
Reason: I am updating the design brief and will also guarantee the payment.

Target Market(s)

Mobile users looking for simplicity

Requirements
Must have
• - Very visually pleasing
- Simple layout with minimal clutter
- Icons and buttons that explain what they do
Should not have
• Any features that detract from the simplicity of the app are not wanted.

```html
<!DOCTYPE html>
<html lang="en">
<head>
<meta charset="utf-8">
<title>Pebble Notes App – Screens</title>
<link href="https://fonts.googleapis.com/css2?family=Advent+Pro:wght@200;300&family=Open+Sans:wght@400;600;700&display=swap" rel="stylesheet">
<style>
  :root{
    --canvas:#e5e5e5;
    --title-blue:#1a6db3;
    --accent:#1b8fd6;
    --accent-dark:#0a6fb8;
    --header-top:#1496df;
    --header-bottom:#63c9f0;
    --header-text:#1d3347;
    --status:#141414;
    --screen-back:#2f3943;
    --card:#f4f5f5;
    --card-edge:#b9bec2;
    --list-back:#dbe2e5;
    --list-active:#c6ced1;
    --divider:#9aa6ac;
    --tab-top:#23a6ec;
    --tab-bottom:#0b82cf;
    --tab-selected:#1e4560;
    --icon-dark:#1b2b38;
    --paper-line:#a9adb0;
    --paper-margin:#d08a9a;
    --hole:#4a4d50;
  }
  *{box-sizing:border-box;margin:0;padding:0}
  html,body{width:1200px;height:1000px;overflow:hidden}
  body{background:var(--canvas);position:relative;font-family:"Open Sans",Arial,sans-serif}

  .app-title{position:absolute;left:300px;width:580px;text-align:center;
    font-family:"Advent Pro",Arial,sans-serif;font-weight:200;color:var(--title-blue);
    font-size:80px;letter-spacing:9px;line-height:1}
  .app-title.line-one{top:150px}
  .app-title.line-two{top:252px}

  .screen{position:absolute;width:237px;height:357px;background:var(--screen-back);overflow:hidden}
  .screen.home{left:44px;top:118px}
  .screen.tasks{left:341px;top:507px}
  .screen.task-detail{left:626px;top:507px}
  .screen.notes{left:914px;top:113px}

  .status-bar{height:16px;background:var(--status);color:#fff;font-size:9px;font-weight:600;
    display:flex;align-items:center;justify-content:space-between;padding:0 5px}
  .status-bar .signal{display:flex;align-items:center;gap:3px}
  .status-bar .bars{display:inline-flex;align-items:flex-end;gap:1px;height:7px}
  .status-bar .bars i{display:block;width:2px;background:#fff}
  .status-bar .battery{width:15px;height:7px;border:1px solid #fff;border-radius:1px;padding:1px}
  .status-bar .battery::after{content:"";display:block;height:100%;background:#fff}

  .nav-header{height:32px;background:linear-gradient(to right,var(--header-top),var(--header-bottom));
    display:flex;align-items:center;justify-content:center;position:relative;
    color:var(--header-text);font-weight:700;font-size:16px}
  .nav-header .new-button{position:absolute;right:8px;top:7px;width:48px;height:17px;border-radius:3px;
    background:#8fd3f0;color:#4a7fa0;font-size:11px;font-weight:700;display:flex;align-items:center;justify-content:center}

  .card{position:absolute;left:4px;width:229px;background:var(--card);border:1px solid var(--card-edge);border-radius:3px}
  .home .card{top:52px;height:261px}
  .tasks .card,.task-detail .card{top:51px;height:261px;left:3px;width:231px}
  .notes .card{top:52px;height:266px;background:#f2f2f2}

  .menu-list{position:absolute;left:7px;top:16px;width:214px;background:var(--list-back)}
  .menu-item{height:55px;display:flex;align-items:center;padding:0 12px 0 12px;border-bottom:1px solid var(--divider);
    color:var(--accent);font-size:12px;font-weight:700;letter-spacing:1.5px}
  .menu-item:last-child{border-bottom:none;height:60px}
  .menu-item.active{background:var(--list-active)}
  .menu-item svg.icon{width:22px;height:22px;margin-right:16px}
  .menu-item .label{flex:1}
  .menu-item svg.chevron{width:10px;height:14px}

  .task-list{position:absolute;left:7px;top:23px;width:214px;height:191px;background:var(--list-back)}
  .task-row{height:30px;display:flex;align-items:center;justify-content:space-between;padding:0 14px 0 10px;
    border-bottom:1px solid var(--divider);color:var(--accent);font-size:11.5px;font-weight:600;letter-spacing:1px}
  .task-row svg{width:15px;height:15px}

  .detail-row{position:absolute;left:17px;top:28px;display:flex;align-items:center}
  .detail-row .label{color:var(--accent);font-weight:700;font-size:13px;letter-spacing:2px;width:95px}
  .detail-button{width:41px;height:16px;border-radius:2px;margin-right:14px;display:flex;align-items:center;justify-content:center;
    background:linear-gradient(var(--tab-top),var(--accent-dark));color:var(--icon-dark);font-size:11px;font-weight:700}
  .detail-button.info{background:linear-gradient(#5cc2ee,#2c9ddc)}

  .paper{position:absolute;left:4px;top:6px;width:219px;height:252px;background:#fbfbfb;border:1px solid #cfd2d4;overflow:hidden}
  .paper .margin-line{position:absolute;left:20px;top:0;bottom:0;width:1px;background:var(--paper-margin)}
  .paper .rule{position:absolute;left:20px;right:8px;height:1px;background:var(--paper-line)}
  .paper .hole{position:absolute;left:5px;width:9px;height:9px;border-radius:50%;background:var(--hole)}
  .paper .note-text{position:absolute;left:28px;top:12px;width:180px;font-size:8.6px;line-height:16.8px;color:#333;letter-spacing:.3px}
  .paper .scrollbar{position:absolute;right:3px;top:10px;width:5px;height:238px;border-radius:3px;background:#d5d8da}
  .paper .scrollbar::after{content:"";display:block;width:5px;height:70px;margin-top:18px;border-radius:3px;background:#8d9296}

  .tab-bar{position:absolute;left:0;right:0;height:32px;background:linear-gradient(var(--tab-top),var(--tab-bottom));
    display:flex;align-items:center;justify-content:space-around;padding:0 4px}
  .tasks .tab-bar,.task-detail .tab-bar{top:324px}
  .notes .tab-bar{top:325px}
  .tab{width:38px;height:30px;display:flex;align-items:center;justify-content:center;border-radius:3px}
  .tab.selected{background:var(--tab-selected)}
  .tab svg{width:22px;height:22px}
</style>
</head>
<body>

  <h1 class="app-title line-one">PEBBLE NOTES</h1>
  <div class="app-title line-two">APP</div>

  <!-- Home screen -->
  <section class="screen home">
    <div class="status-bar">
      <span class="signal"><span class="bars"><i style="height:2px"></i><i style="height:3px"></i><i style="height:5px"></i><i style="height:7px"></i></span>3G</span>
      <span>9:41 AM</span><span class="battery"></span>
    </div>
    <header class="nav-header">PEBBLE NOTES</header>
    <div class="card">
      <nav class="menu-list">
        <div class="menu-item active">
          <svg class="icon" viewBox="0 0 22 22"><rect x="1.5" y="1.5" width="19" height="19" fill="none" stroke="#1b8fd6" stroke-width="1.6"/><path d="M5 11l4 4 8-9" fill="none" stroke="#1b8fd6" stroke-width="2"/></svg>
          <span class="label">TASK</span>
          <svg class="chevron" viewBox="0 0 10 14"><path d="M2 1l6 6-6 6" fill="none" stroke="#1b8fd6" stroke-width="2.6"/></svg>
        </div>
        <div class="menu-item">
          <svg class="icon" viewBox="0 0 22 22"><rect x="2" y="3" width="15" height="18" fill="none" stroke="#1b8fd6" stroke-width="1.4"/><path d="M4 2v3M7 2v3M10 2v3M13 2v3" stroke="#1b8fd6" stroke-width="1.2"/><path d="M9 17l2-5 8-8 3 3-8 8z" fill="#fff" stroke="#1b8fd6" stroke-width="1.4"/></svg>
          <span class="label">NOTES</span>
          <svg class="chevron" viewBox="0 0 10 14"><path d="M2 1l6 6-6 6" fill="none" stroke="#1b8fd6" stroke-width="2.6"/></svg>
        </div>
        <div class="menu-item">
          <svg class="icon" viewBox="0 0 22 22"><path d="M11 4v14M4 11h14" stroke="#1b8fd6" stroke-width="4"/></svg>
          <span class="label">MORE</span>
          <svg class="chevron" viewBox="0 0 10 14"><path d="M2 1l6 6-6 6" fill="none" stroke="#1b8fd6" stroke-width="2.6"/></svg>
        </div>
      </nav>
    </div>
  </section>

  <!-- Task list screen -->
  <section class="screen tasks">
    <div class="status-bar">
      <span class="signal"><span class="bars"><i style="height:2px"></i><i style="height:3px"></i><i style="height:5px"></i><i style="height:7px"></i></span>3G</span>
      <span>9:41 AM</span><span class="battery"></span>
    </div>
    <header class="nav-header">TASK</header>
    <div class="card">
      <div class="task-list">
        <div class="task-row"><span>Buy DVD</span>
          <svg viewBox="0 0 15 15"><rect x="0.75" y="0.75" width="13.5" height="13.5" fill="#fff" stroke="#1b8fd6" stroke-width="1.5"/><path d="M3.5 7.5l3 3 5-6" fill="none" stroke="#1b8fd6" stroke-width="1.6"/></svg></div>
        <div class="task-row"><span>Watch DVD</span>
          <svg viewBox="0 0 15 15"><rect x="0.75" y="0.75" width="13.5" height="13.5" fill="#fff" stroke="#1b8fd6" stroke-width="1.5"/></svg></div>
      </div>
    </div>
    <nav class="tab-bar">
      <span class="tab"><svg viewBox="0 0 22 22"><rect x="2" y="2" width="18" height="18" fill="none" stroke="#1b2b38" stroke-width="1.6"/><path d="M5 7h12M5 11h12M5 15h12" stroke="#1b2b38" stroke-width="1.8"/></svg></span>
      <span class="tab selected"><svg viewBox="0 0 22 22"><rect x="2" y="2" width="18" height="18" fill="none" stroke="#23a6ec" stroke-width="1.6"/><path d="M5 11l4 4 8-9" fill="none" stroke="#23a6ec" stroke-width="2"/></svg></span>
      <span class="tab"><svg viewBox="0 0 22 22"><rect x="2" y="3" width="15" height="18" fill="none" stroke="#1b2b38" stroke-width="1.4"/><path d="M4 2v3M7 2v3M10 2v3M13 2v3" stroke="#1b2b38" stroke-width="1.2"/><path d="M9 17l2-5 8-8 3 3-8 8z" fill="none" stroke="#1b2b38" stroke-width="1.4"/></svg></span>
      <span class="tab"><svg viewBox="0 0 22 22"><path d="M11 3v16M3 11h16" stroke="#1b2b38" stroke-width="4"/></svg></span>
    </nav>
  </section>

  <!-- Task detail screen -->
  <section class="screen task-detail">
    <div class="status-bar">
      <span class="signal"><span class="bars"><i style="height:2px"></i><i style="height:3px"></i><i style="height:5px"></i><i style="height:7px"></i></span>3G</span>
      <span>9:41 AM</span><span class="battery"></span>
    </div>
    <header class="nav-header">Buy DVD</header>
    <div class="card">
      <div class="detail-row">
        <span class="label">Save</span>
        <span class="detail-button">!</span>
        <span class="detail-button info"><svg width="11" height="11" viewBox="0 0 11 11"><circle cx="5.5" cy="5.5" r="4.5" fill="none" stroke="#1b2b38" stroke-width="1"/><path d="M5.5 4.5v4" stroke="#1b2b38" stroke-width="1"/></svg></span>
      </div>
    </div>
    <nav class="tab-bar">
      <span class="tab"><svg viewBox="0 0 22 22"><rect x="2" y="2" width="18" height="18" fill="none" stroke="#1b2b38" stroke-width="1.6"/><path d="M5 7h12M5 11h12M5 15h12" stroke="#1b2b38" stroke-width="1.8"/></svg></span>
      <span class="tab selected"><svg viewBox="0 0 22 22"><rect x="2" y="2" width="18" height="18" fill="none" stroke="#23a6ec" stroke-width="1.6"/><path d="M5 11l4 4 8-9" fill="none" stroke="#23a6ec" stroke-width="2"/></svg></span>
      <span class="tab"><svg viewBox="0 0 22 22"><rect x="2" y="3" width="15" height="18" fill="none" stroke="#1b2b38" stroke-width="1.4"/><path d="M4 2v3M7 2v3M10 2v3M13 2v3" stroke="#1b2b38" stroke-width="1.2"/><path d="M9 17l2-5 8-8 3 3-8 8z" fill="none" stroke="#1b2b38" stroke-width="1.4"/></svg></span>
      <span class="tab"><svg viewBox="0 0 22 22"><path d="M11 3v16M3 11h16" stroke="#1b2b38" stroke-width="4"/></svg></span>
    </nav>
  </section>

  <!-- Notes screen -->
  <section class="screen notes">
    <div class="status-bar">
      <span class="signal"><span class="bars"><i style="height:2px"></i><i style="height:3px"></i><i style="height:5px"></i><i style="height:7px"></i></span>3G</span>
      <span>9:41 AM</span><span class="battery"></span>
    </div>
    <header class="nav-header">NOTES<span class="new-button">NEW</span></header>
    <div class="card">
      <div class="paper">
        <span class="margin-line"></span>
        <span class="rule" style="top:28px"></span><span class="rule" style="top:45px"></span>
        <span class="rule" style="top:62px"></span><span class="rule" style="top:79px"></span>
        <span class="rule" style="top:96px"></span><span class="rule" style="top:120px"></span>
        <span class="rule" style="top:144px"></span><span class="rule" style="top:168px"></span>
        <span class="rule" style="top:192px"></span><span class="rule" style="top:216px"></span>
        <span class="rule" style="top:240px"></span>
        <span class="hole" style="top:18px"></span><span class="hole" style="top:42px"></span>
        <span class="hole" style="top:66px"></span><span class="hole" style="top:90px"></span>
        <span class="hole" style="top:114px"></span><span class="hole" style="top:138px"></span>
        <span class="hole" style="top:162px"></span><span class="hole" style="top:186px"></span>
        <span class="hole" style="top:210px"></span><span class="hole" style="top:234px"></span>
        <p class="note-text">Lorem ipsum dolor sit amet, consec-tetuer adipiscing elit, sed diam non-ummy nibh euismod tincidunt ut lao-reet dolore magna aliquam erat vo-lutpat</p>
        <span class="scrollbar"></span>
      </div>
    </div>
    <nav class="tab-bar">
      <span class="tab"><svg viewBox="0 0 22 22"><rect x="2" y="2" width="18" height="18" fill="none" stroke="#1b2b38" stroke-width="1.6"/><path d="M5 7h12M5 11h12M5 15h12" stroke="#1b2b38" stroke-width="1.8"/></svg></span>
      <span class="tab"><svg viewBox="0 0 22 22"><rect x="2" y="2" width="18" height="18" fill="none" stroke="#1b2b38" stroke-width="1.6"/><path d="M5 11l4 4 8-9" fill="none" stroke="#1b2b38" stroke-width="2"/></svg></span>
      <span class="tab selected"><svg viewBox="0 0 22 22"><rect x="2" y="3" width="15" height="18" fill="none" stroke="#23a6ec" stroke-width="1.4"/><path d="M4 2v3M7 2v3M10 2v3M13 2v3" stroke="#23a6ec" stroke-width="1.2"/><path d="M9 17l2-5 8-8 3 3-8 8z" fill="none" stroke="#23a6ec" stroke-width="1.4"/></svg></span>
      <span class="tab"><svg viewBox="0 0 22 22"><path d="M11 3v16M3 11h16" stroke="#1b2b38" stroke-width="4"/></svg></span>
    </nav>
  </section>

</body>
</html>
```